Trading Company needs a business card design, letter head design and email signature

We need a double-sided business card design, letter head design and an email signature. We have a logo design.

Possible Tag Lines:
• “Connecting Worlds, Building Excellence.”
• “Global Sourcing, Local Excellence.”
• “Bridging Borders, Building Quality.”
• “Worldwide Partnerships, Superior Goods.”
• “Where Quality Meets Affordability”

Services Offered:
Procurement
Fabrication
Distribution
Logistics
Import/Export

Requirements
Must have
• Nice quality double sided Business Card design, Letterhead design needs to be A4
Nice to have
• possible ideas on tag lines

```html
<!DOCTYPE html>
<html lang="en">
<head>
<meta charset="utf-8">
<title>Tradeva Stationery</title>
<link href="https://fonts.googleapis.com/css2?family=Arimo:wght@400;700&family=Jost:wght@500&display=swap" rel="stylesheet">
<style>
  :root {
    --brand-red: #ed2327;
    --brand-grey: #58595b;
    --ink: #4a4a4c;
    --muted: #6d6e71;
    --paper: #ffffff;
    --backdrop: #9a9899;
  }
  * { margin: 0; padding: 0; box-sizing: border-box; }
  html, body { width: 1200px; height: 930px; overflow: hidden; }
  body { background: var(--backdrop); font-family: "Arimo", Arial, sans-serif; color: var(--ink); position: relative; }

  .sheet { position: absolute; background: var(--paper); box-shadow: 3px 4px 6px rgba(0,0,0,.35); overflow: hidden; }
  .footer-band { position: absolute; left: 0; bottom: 0; width: 100%; }
  .footer-url { position: absolute; right: 0; color: #fff; text-align: right; }

  .wordmark { font-family: "Arimo", Arial, sans-serif; font-weight: 700; color: var(--brand-red); letter-spacing: .06em; display: flex; align-items: center; white-space: nowrap; }
  .wordmark .mark { display: inline-block; background: var(--brand-red); margin-right: .35em; }
  .wordmark--white { color: #fff; }

  .icon { display: inline-block; vertical-align: middle; }

  /* Letterhead */
  .letterhead { left: 49px; top: 117px; width: 492px; height: 696px; }
  .letterhead .wordmark { position: absolute; left: 42px; top: 68px; font-size: 20px; }
  .letterhead .wordmark .mark { width: 14px; height: 14px; }
  .letterhead-contact { position: absolute; left: 350px; top: 32px; border-left: 1px solid var(--muted); padding-left: 7px; font-size: 7.8px; line-height: 10px; color: var(--muted); }
  .letterhead-contact p + p { margin-top: 7px; }
  .letterhead-contact .line { display: flex; align-items: center; gap: 4px; }
  .letter-greeting { position: absolute; left: 44px; top: 214px; font-family: "Jost", sans-serif; font-weight: 500; font-size: 11.5px; color: var(--ink); }
  .letter-body { position: absolute; left: 44px; top: 246px; width: 405px; font-size: 8.1px; line-height: 10.2px; color: var(--muted); }
  .letter-body p + p { margin-top: 8.5px; }
  .letter-closing { position: absolute; left: 44px; top: 456px; font-size: 6.5px; font-weight: 700; color: var(--ink); }
  .letterhead .footer-url { bottom: 4px; right: 25px; font-size: 8px; }

  /* Business card front */
  .card-front { left: 574px; top: 119px; width: 343px; height: 196px; }
  .card-front .wordmark { position: absolute; right: 19px; top: 85px; font-size: 25px; }
  .card-front .wordmark .mark { width: 18px; height: 18px; }
  .card-holder { position: absolute; left: 19px; top: 107px; }
  .card-holder .name { color: var(--brand-red); font-weight: 700; font-size: 12px; }
  .card-holder .role { color: var(--muted); font-size: 9.5px; margin-top: 1px; }
  .card-rule { position: absolute; left: 19px; top: 134px; width: 305px; height: 1px; background: var(--muted); }
  .card-contact { position: absolute; left: 19px; top: 145px; font-size: 9.5px; line-height: 13px; color: var(--muted); }
  .card-contact .line { display: flex; align-items: center; gap: 5px; }
  .card-address { position: absolute; right: 19px; top: 146px; font-size: 9.5px; line-height: 12px; text-align: right; color: var(--muted); }
  .card-front .footer-url { bottom: 2px; right: 20px; font-size: 10.5px; }

  /* Business card back */
  .card-back { left: 574px; top: 353px; width: 343px; height: 195px; background: var(--brand-red); }
  .card-back .wordmark { position: absolute; left: 14px; top: 16px; font-size: 24px; }
  .card-back .wordmark .mark { background: #fff; width: 17px; height: 17px; }
  .services { position: absolute; left: 15px; top: 79px; color: #fff; }
  .services h2 { font-size: 10.5px; font-weight: 700; margin-bottom: 2px; }
  .services ul { list-style: none; font-size: 10.5px; line-height: 13px; }
  .services li { display: flex; align-items: center; gap: 4px; }
  .tagline { position: absolute; left: 15px; top: 165px; color: #fff; font-size: 10.5px; }

  /* Email signature */
  .signature { left: 575px; top: 578px; width: 574px; height: 235px; }
  .signature .wordmark { position: absolute; left: 52px; top: 130px; font-size: 33px; }
  .signature .wordmark .mark { width: 24px; height: 24px; }
  .signature-divider { position: absolute; left: 284px; top: 34px; width: 2px; height: 147px; background: var(--muted); }
  .signature-details { position: absolute; left: 304px; top: 26px; }
  .signature-details .name { color: var(--brand-red); font-weight: 700; font-size: 24px; line-height: 26px; }
  .signature-details .role { color: var(--muted); font-size: 19px; line-height: 22px; }
  .signature-details .address { color: var(--muted); font-size: 19px; line-height: 22px; margin-top: 9px; }
  .signature-details .contact { margin-top: 11px; color: var(--muted); font-size: 19px; line-height: 25px; }
  .signature-details .line { display: flex; align-items: center; gap: 9px; }
  .signature .footer-url { bottom: 3px; right: 25px; font-size: 19px; }
</style>
</head>
<body>

<!-- Letterhead -->
<section class="sheet letterhead">
  <div class="wordmark"><span class="mark"></span>TRADEVA</div>
  <div class="letterhead-contact">
    <p>Your Address, City<br>State, Zip 0000</p>
    <p>
      <span class="line"><svg class="icon" width="7" height="7" viewBox="0 0 10 10"><path d="M2 1 L4 1 L4.6 3.2 L3.4 4 Q4.5 6 6 6.6 L6.8 5.4 L9 6 L9 8 Q5 9.5 1 3 Z" fill="#ed2327"/></svg>555-014-2290</span>
      <span class="line"><svg class="icon" width="7" height="6" viewBox="0 0 10 8"><rect x=".6" y=".6" width="8.8" height="6.8" fill="none" stroke="#ed2327" stroke-width="1.2"/><path d="M.6 .6 L5 4.5 L9.4 .6" fill="none" stroke="#ed2327" stroke-width="1.2"/></svg>hello@tradeva.example</span>
    </p>
  </div>
  <h1 class="letter-greeting">Dear Mr. Brooks,</h1>
  <div class="letter-body">
    <p>Lorem ipsum dolor sit amet, consectetuer adipiscing elit, sed diam nonmmy nibh euismod tincidunt ut laor eet dolore magna aliquam erat volutpat. Ut wisi enim ad minim veniam, quis nostrud exerci tationmcorper suscipit lobortis nisl ut aliquip ex ea commodo consequat. Duis autem vel eum iriure dolor in hendrerit in vulputate velit esse molestie consequat, vel illum dolore eu feugiat</p>
    <p>Rorem ipsum dolor sit amet, consectetuer adipiscing elit, sed diam nonmmy nibh euismod tincidunt ut laor eet dolore magna aliquam erat volutpat. Ut wisi enim ad minim veniam, quis nostrud exerci tationmcorper suscipit lobortis nisl ut aliquip ex ea commodo consequat. Duis autem vel eum iriure dolor in hendrerit in vulputate velit esse molest</p>
    <p>Dorem ipsum dolor sit amet, consectetuer adipiscing elit, sed diam nonmmy nibh euismod tincidunt ut laor eet dolore magna aliquam erat volutpat. Ut wisi enim ad minim veniam, quis nostrud exerci tationmcorper suscipit lobortis nisl ut aliquip ex ea commodo consequat. Duis autem vel eum iriure dolor in hendrerit in suscipit lobortis nisl ut aliquip ex ea commodo consequat. Duis autem vel eum iriure dolor in hendrerit in vulputate velit esse molestie consequat, vel illum</p>
    <p>Sorem ipsum dolor sit amet, consectetuer adipiscing elit, sed diam nonmmy nibh euismod tincidunt ut laor eet dolore magna aliquam erat volutpat. Ut wisi enim ad minim veniam, quis nostrud exerci tationmcorper suscipit lobortis nisl ut aliquip ex ea commodo consequat. Duis autem vel eum iriure dolor in</p>
  </div>
  <p class="letter-closing">Sincerely,</p>
  <svg class="footer-band" width="492" height="17" viewBox="0 0 492 17" preserveAspectRatio="none">
    <rect x="0" y="9" width="310" height="8" fill="#58595b"/>
    <polygon points="304,17 320,0 492,0 492,17" fill="#fff"/>
    <polygon points="310,17 326,0 492,0 492,17" fill="#ed2327"/>
  </svg>
  <span class="footer-url">www.tradeva.example</span>
</section>

<!-- Business card front -->
<section class="sheet card-front">
  <div class="wordmark"><span class="mark"></span>TRADEVA</div>
  <div class="card-holder">
    <p class="name">DANIEL BROOKS</p>
    <p class="role">Manager</p>
  </div>
  <div class="card-rule"></div>
  <div class="card-contact">
    <span class="line"><svg class="icon" width="8" height="8" viewBox="0 0 10 10"><path d="M2 1 L4 1 L4.6 3.2 L3.4 4 Q4.5 6 6 6.6 L6.8 5.4 L9 6 L9 8 Q5 9.5 1 3 Z" fill="#ed2327"/></svg>555-014-2290</span>
    <span class="line"><svg class="icon" width="8" height="7" viewBox="0 0 10 8"><rect x=".6" y=".6" width="8.8" height="6.8" fill="none" stroke="#ed2327" stroke-width="1.2"/><path d="M.6 .6 L5 4.5 L9.4 .6" fill="none" stroke="#ed2327" stroke-width="1.2"/></svg>hello@tradeva.example</span>
  </div>
  <p class="card-address">Your Address, City<br>State, Zip 0000</p>
  <svg class="footer-band" width="343" height="17" viewBox="0 0 343 17" preserveAspectRatio="none">
    <rect x="0" y="9" width="175" height="8" fill="#58595b"/>
    <polygon points="170,17 185,0 343,0 343,17" fill="#fff"/>
    <polygon points="176,17 191,0 343,0 343,17" fill="#ed2327"/>
  </svg>
  <span class="footer-url">www.tradeva.example</span>
</section>

<!-- Business card back -->
<section class="sheet card-back">
  <div class="wordmark wordmark--white"><span class="mark"></span>TRADEVA</div>
  <div class="services">
    <h2>SERVICES OFFERED:</h2>
    <ul>
      <li><svg class="icon" width="8" height="8" viewBox="0 0 10 10"><path d="M5 0 L10 5 L5 10 L0 5 Z" fill="#fff"/></svg>Procurement</li>
      <li><svg class="icon" width="8" height="8" viewBox="0 0 10 10"><path d="M5 0 L10 5 L5 10 L0 5 Z" fill="#fff"/></svg>Fabrication</li>
      <li><svg class="icon" width="8" height="8" viewBox="0 0 10 10"><path d="M5 0 L10 5 L5 10 L0 5 Z" fill="#fff"/></svg>Distribution</li>
      <li><svg class="icon" width="8" height="8" viewBox="0 0 10 10"><path d="M5 0 L10 5 L5 10 L0 5 Z" fill="#fff"/></svg>Logistics</li>
      <li><svg class="icon" width="8" height="8" viewBox="0 0 10 10"><path d="M5 0 L10 5 L5 10 L0 5 Z" fill="#fff"/></svg>Import/Export</li>
    </ul>
  </div>
  <p class="tagline">Connecting Worlds, Building Excellence</p>
</section>

<!-- Email signature -->
<section class="sheet signature">
  <div class="wordmark"><span class="mark"></span>TRADEVA</div>
  <div class="signature-divider"></div>
  <div class="signature-details">
    <p class="name">DANIEL BROOKS</p>
    <p class="role">Manager</p>
    <p class="address">Your Address<br>City, State, Zip 0000</p>
    <div class="contact">
      <span class="line"><svg class="icon" width="15" height="15" viewBox="0 0 10 10"><path d="M2 1 L4 1 L4.6 3.2 L3.4 4 Q4.5 6 6 6.6 L6.8 5.4 L9 6 L9 8 Q5 9.5 1 3 Z" fill="#ed2327"/></svg>555-014-2290</span>
      <span class="line"><svg class="icon" width="15" height="12" viewBox="0 0 10 8"><rect x=".6" y=".6" width="8.8" height="6.8" fill="none" stroke="#ed2327" stroke-width="1"/><path d="M.6 .6 L5 4.5 L9.4 .6" fill="none" stroke="#ed2327" stroke-width="1"/></svg>hello@tradeva.example</span>
    </div>
  </div>
  <svg class="footer-band" width="574" height="27" viewBox="0 0 574 27" preserveAspectRatio="none">
    <rect x="0" y="13" width="300" height="14" fill="#58595b"/>
    <polygon points="288,27 312,0 574,0 574,27" fill="#fff"/>
    <polygon points="298,27 322,0 574,0 574,27" fill="#ed2327"/>
  </svg>
  <span class="footer-url">www.tradeva.example</span>
</section>

</body>
</html>
```